Business Card & Stationery
Larkspur Renewal
Project: Business Card & Stationery
Business Card & Stationery  - Health
Creative Brief
Simple
Thomas Valdoroni, DNP, RN, APN-C
418 West Birch Avenue Suite 5K Moorestown, NJ 08057
LarkspurRenewal@postvale.example
www.LarkspurRenewal.example
There are two logs attached, one with white background and one with beige background. You can use either color in your design

```html
<!DOCTYPE html>
<html lang="en">
<head>
<meta charset="utf-8">
<title>Larkspur Renewal — Business Card &amp; Stationery</title>
<link rel="stylesheet" href="https://fonts.googleapis.com/css2?family=Lato:wght@400;700&display=swap">
<style>
  :root {
    --backdrop: #e6e6e6;
    --paper: #ffffff;
    --cream: #fbefc0;
    --ink: #222222;
    --ink-soft: #555555;
    --mark: #1d1d1d;
    --lamp: #f2d23a;
    --ghost: #f3f1ea;
    --shadow: 0 2px 5px rgba(0,0,0,.18);
  }
  * { margin: 0; padding: 0; box-sizing: border-box; }
  html, body { width: 1200px; height: 820px; overflow: hidden; background: var(--backdrop); font-family: "Lato", sans-serif; color: var(--ink); }
  .canvas { position: relative; width: 1200px; height: 820px; }

  .sheet { position: absolute; background: var(--paper); box-shadow: var(--shadow); }
  .letterhead { left: 38px; top: 43px; width: 516px; height: 737px; }

  .brand { position: absolute; display: flex; align-items: center; gap: 8px; background: var(--paper); padding: 6px 10px; }
  .brand-square { width: 14px; height: 14px; background: var(--mark); flex: none; }
  .brand-text { display: flex; flex-direction: column; }
  .brand-name { font-weight: 700; font-size: 19px; line-height: 1.1; color: var(--mark); letter-spacing: .5px; white-space: nowrap; }
  .brand-tag { font-size: 6px; line-height: 1.2; letter-spacing: 1.5px; color: var(--ink-soft); text-transform: uppercase; margin-top: 2px; white-space: nowrap; }

  .letterhead .brand { left: 8px; top: 8px; }

  .ghost-mark { position: absolute; background: var(--ghost); border-radius: 40px 40px 6px 6px; }
  .letterhead .ghost-mark { left: 190px; top: 233px; width: 170px; height: 312px; }

  .footer-line { position: absolute; display: flex; gap: 16px; font-size: 6.5px; line-height: 1; color: var(--ink-soft); white-space: nowrap; }
  .letterhead .footer-line { left: 124px; top: 718px; }

  .card { position: absolute; width: 221px; height: 132px; border-radius: 10px; box-shadow: var(--shadow); display: flex; flex-direction: column; align-items: center; }
  .card-white { left: 631px; top: 216px; background: var(--paper); }
  .card-cream { left: 871px; top: 216px; background: var(--cream); }
  .card .brand { position: static; background: transparent; margin-top: 38px; }
  .card .brand-name { font-size: 16px; }
  .card-web { position: absolute; bottom: 14px; font-size: 6.5px; color: var(--ink-soft); white-space: nowrap; }

  .envelope { position: absolute; left: 590px; top: 403px; width: 569px; height: 377px; background: var(--paper); box-shadow: var(--shadow); border-radius: 14px 14px 0 0; overflow: hidden; }
  .envelope-flap { position: absolute; left: 0; top: 0; width: 100%; height: 149px; background: var(--cream); }
  .flap-icon { position: absolute; left: 264px; top: 12px; }
  .envelope .brand { left: 17px; top: 92px; }
  .envelope .ghost-mark { left: 418px; top: 149px; width: 144px; height: 216px; border-radius: 30px 30px 4px 4px; }
  .envelope .footer-line { left: 18px; top: 355px; }
</style>
</head>
<body>
<main class="canvas">

  <section class="sheet letterhead">
    <div class="brand">
      <span class="brand-square"></span>
      <div class="brand-text">
        <span class="brand-name">Larkspur Renewal</span>
        <span class="brand-tag">Nurse practitioner care services</span>
      </div>
    </div>
    <div class="ghost-mark" role="img" aria-label="Faint brand lantern emblem"></div>
    <div class="footer-line">
      <span>856-555-0143</span>
      <span>418 West Birch Avenue Suite 5K Alderbrook, NJ 08199</span>
      <span>LarkspurRenewal@postvale.example</span>
    </div>
  </section>

  <section class="card card-white">
    <div class="brand">
      <span class="brand-square"></span>
      <div class="brand-text">
        <span class="brand-name">Larkspur Renewal</span>
        <span class="brand-tag">Nurse practitioner care services</span>
      </div>
    </div>
    <span class="card-web">www.LarkspurRenewal.example</span>
  </section>

  <section class="card card-cream">
    <div class="brand">
      <span class="brand-square"></span>
      <div class="brand-text">
        <span class="brand-name">Larkspur Renewal</span>
        <span class="brand-tag">Nurse practitioner care services</span>
      </div>
    </div>
    <span class="card-web">www.LarkspurRenewal.example</span>
  </section>

  <section class="envelope">
    <div class="envelope-flap">
      <svg class="flap-icon" width="40" height="48" viewBox="0 0 40 48" role="img" aria-label="Brand square">
        <rect x="6" y="10" width="28" height="28" fill="var(--mark)"/>
        <rect x="11" y="15" width="18" height="18" fill="var(--lamp)"/>
      </svg>
    </div>
    <div class="brand">
      <span class="brand-square"></span>
      <div class="brand-text">
        <span class="brand-name">Larkspur Renewal</span>
        <span class="brand-tag">Nurse practitioner care services</span>
      </div>
    </div>
    <div class="ghost-mark" role="img" aria-label="Faint brand lantern emblem"></div>
    <div class="footer-line">
      <span>418 West Birch Avenue Suite 5K Alderbrook, NJ 08199</span>
      <span>856-555-0143</span>
      <span>LarkspurRenewal@postvale.example</span>
    </div>
  </section>

</main>
</body>
</html>
```